BBS Challenge Graphics for a Challenge

I want to create 9-10 social media graphics (new Instagram size 4:5 (1080 x 1350 pixels) focusing on our next 10-Day Berry Blend Sprint. Use any of the pics in the dropbox, NO RANDOM STOCK PHOTOGRAPHY. For the color scheme of the graphics, they should all be complementary to the green smoothie book attached.
You can add any of the photos as they are all posted here. You do NOT need to access Dropbox now. (all the details in the word document) NOTE: The date is Monday 12/8!
Updates

All of the images are now posted here. You do NOT need to access the Dropbox.

PLEASE NOTE THE DATE OF THIS CHALLENGE IS MONDAY, 12/8!

Target Market(s)

women and men

Requirements
Must have
• the text and pics in the Dropbox

```html
<!DOCTYPE html>
<html lang="en">
<head>
<meta charset="utf-8">
<title>10-Day Berry Blend Sprint</title>
<link href="https://fonts.googleapis.com/css2?family=Jost:wght@500;600&display=swap" rel="stylesheet">
<style>
  :root {
    --green-top: #2f9a45;
    --green-mid: #5fa36a;
    --mauve-mid: #b58a9a;
    --pink-bottom: #d569a8;
    --pink-deep: #c95a98;
    --text: #ffffff;
    --rule: rgba(255, 255, 255, 0.92);
  }
  html, body {
    margin: 0;
    padding: 0;
    width: 960px;
    height: 1200px;
    overflow: hidden;
    background: var(--pink-bottom);
  }
  .post {
    position: relative;
    width: 960px;
    height: 1200px;
    overflow: hidden;
    font-family: "Jost", "Futura", sans-serif;
    color: var(--text);
  }
  .post__photo {
    position: absolute;
    inset: 0;
    background:
      radial-gradient(ellipse at 30% 25%, rgba(255,255,255,0.10), transparent 55%),
      linear-gradient(180deg,
        var(--green-top) 0%,
        var(--green-mid) 30%,
        var(--mauve-mid) 58%,
        var(--pink-deep) 80%,
        var(--pink-bottom) 100%);
  }
  .headline {
    position: absolute;
    left: 0;
    width: 986px;
    margin: 0;
    text-align: center;
    font-weight: 500;
    font-size: 84px;
    line-height: 76px;
    letter-spacing: 0.5px;
    text-transform: uppercase;
    text-shadow: 0 2px 6px rgba(0, 0, 0, 0.28);
  }
  .headline--title { top: 331px; }
  .headline--date { top: 615px; }
  .headline--promise { top: 909px; }
  .divider {
    position: absolute;
    left: 300px;
    width: 392px;
    height: 3px;
    background: var(--rule);
    box-shadow: 0 1px 4px rgba(0, 0, 0, 0.2);
  }
  .divider--first { top: 583px; }
  .divider--second { top: 877px; }
</style>
</head>
<body>
  <main class="post">
    <div class="post__photo" role="img" aria-label="Photo of the smiling host holding up a gummy and a supplement bottle, tinted with a green-to-pink overlay"></div>

    <h1 class="headline headline--title">10-Day Berry<br>Blend<br>Sprint</h1>
    <div class="divider divider--first"></div>
    <p class="headline headline--date">Begins<br>Monday<br>12/8!</p>
    <div class="divider divider--second"></div>
    <p class="headline headline--promise">Lose up to<br>15 lbs in<br>10 days!</p>
  </main>
</body>
</html>
```